Math Help Website Needs New Design

Looking to refresh the design of my existing site (quillnumberdesk.com) to be easier on the eyes. I am fully capable of doing the HTML coding and have for years, but I don't have the eye for good design, colors, layout, and fonts. This is where I need help!

I need both a new design scheme and a new logo that matches. The overall functionality will be the same as the existing site, and should not be unrecognizable.

Target Market(s)

It should appeal to students (age 13-22) and their parents, so it should NOT be childish in appearance, nor should it be corporate.

Requirements
Must have
• Should be simple, easy-to-navigate, and neither childish nor corporate. I am looking for a design for both the homepage and a similar "content" page. Simple, bold colors are preferred. A logo should be prominent at the top, with a search bar nearby. Below that I need a similar navigational area like I already have. Then, I need about 200px wide ad space on the left of the main body area.

```html
<!DOCTYPE html>
<html lang="en">
<head>
<meta charset="utf-8">
<title>Quill Number Desk</title>
<link rel="stylesheet" href="https://fonts.googleapis.com/css2?family=Arimo:wght@400;700&family=Source+Sans+3:wght@400;600;700&display=swap">
<style>
:root{
  --sun:#fcc73a;
  --white:#ffffff;
  --ink:#2b2b2b;
  --text:#222;
  --blue:#1e86d2;
  --blue-light:#3aa6ee;
  --blue-dark:#1672c0;
  --nav-active:#3b3b3b;
  --panel:#f2f2f2;
  --footer:#353535;
  --orange:#f0a24a;
  --rust:#8a2a14;
  --ad-yellow:#f3d25a;
  --grey-icon:#8a8a8a;
}
*{margin:0;padding:0;box-sizing:border-box}
html,body{width:1200px;height:1110px;overflow:hidden}
body{position:relative;background:var(--sun);font-family:"Arimo",Arial,sans-serif;color:var(--text)}
.side-art{position:absolute;background:linear-gradient(90deg,#3a2a26,#a8352c)}
.page{position:absolute;left:101px;top:0;width:998px;height:1014px;background:var(--white)}
.header{position:absolute;left:0;top:0;width:998px;height:127px;background:linear-gradient(#ffffff,#f0f0f0)}
.brand{position:absolute;left:16px;top:37px;display:flex;align-items:center;gap:10px;font-family:"Source Sans 3",sans-serif;font-weight:700;font-size:29px;color:var(--blue)}
.brand-dot{width:24px;height:24px;border-radius:50%;background:var(--blue)}
.connect{position:absolute;left:772px;top:13px;font-family:"Source Sans 3",sans-serif;font-weight:700;font-size:19px;color:var(--grey-icon)}
.icons{position:absolute;left:877px;top:10px;display:flex;gap:3px;align-items:center}
.search{position:absolute;left:719px;top:79px;width:220px;height:38px;border-radius:19px;background:linear-gradient(#e6e6e6,#f8f8f8);border:1px solid #d0d0d0;font-size:12px;color:#888;padding:11px 0 0 18px}
.go{position:absolute;left:946px;top:79px;width:41px;height:36px;border-radius:12px;background:linear-gradient(var(--blue-light),var(--blue-dark));color:#fff;font-family:"Source Sans 3",sans-serif;font-weight:700;font-size:19px;text-align:center;line-height:36px}
.nav{position:absolute;left:0;top:127px;width:998px;height:35px;background:linear-gradient(var(--blue-light),var(--blue-dark))}
.nav a{position:absolute;top:0;height:35px;line-height:34px;color:#fff;font-family:"Source Sans 3",sans-serif;font-size:13px;text-align:center;text-decoration:none;border-left:1px solid rgba(255,255,255,.35)}
.nav a.active{background:var(--nav-active);border-left:none}
.ad{position:absolute;left:9px;top:180px;width:202px;height:641px}
.ad-head{position:absolute;left:0;top:0;width:202px;height:126px;background:#f2b25b;border-radius:0 0 50% 50%/0 0 30px 30px;text-align:center;font-family:"Source Sans 3",sans-serif;font-weight:700;font-size:26px;line-height:34px;color:var(--rust);padding-top:22px}
.ad-photo{position:absolute;left:0;top:150px;width:202px;height:372px;background:linear-gradient(#efe6df,#d48a4a 60%,#c86a2c)}
.ad-band{position:absolute;left:0;top:522px;width:202px;height:24px;background:#e99a2e;color:#fff;font-size:11px;font-weight:700;text-align:center;line-height:24px}
.ad-foot{position:absolute;left:0;top:546px;width:202px;height:95px;background:#9a3a1c}
.ad-phone{position:absolute;left:0;top:549px;width:202px;text-align:center;font-family:"Source Sans 3",sans-serif;font-weight:700;font-size:27px;color:var(--ad-yellow)}
.ad-small{position:absolute;left:0;top:587px;width:202px;text-align:center;font-size:8px;color:#fff}
.ad-url{position:absolute;left:24px;top:614px;font-size:8px;color:#fff}
.ad-badge{position:absolute;left:158px;top:605px;width:34px;height:28px;background:#fff}
.chat-art{position:absolute;left:80px;top:845px;width:78px;height:70px;background:linear-gradient(#e7eef5,#2f6ea8)}
.chat{position:absolute;left:12px;top:918px;width:192px;height:71px;border-radius:16px;background:linear-gradient(#3b74a8,#0d3f78);border:2px solid #2a5a8a;text-align:center;color:#fff;font-size:12px;line-height:17px;padding-top:9px}
.chat b{color:#f7c843;font-size:11px;display:block}
.hero{position:absolute;left:227px;top:180px;width:750px;height:313px;background:#fff;box-shadow:0 0 3px rgba(0,0,0,.25)}
.hero-photo{position:absolute;left:10px;top:9px;width:729px;height:294px;background:linear-gradient(90deg,#6b7f5a,#4f7fb5 25%,#78a35a 45%,#c04a7a 65%,#d9d28a 80%,#d38aa8)}
.welcome{position:absolute;left:226px;top:512px;font-family:"Source Sans 3",sans-serif;font-weight:700;font-size:24px;color:var(--ink)}
.welcome span{color:var(--blue)}
.intro{position:absolute;width:490px;font-size:12.5px;line-height:20px;color:var(--text)}
.study-photo{position:absolute;left:721px;top:540px;width:252px;height:168px;background:linear-gradient(90deg,#f4efe8,#3b3b3b 50%,#2e2e2e);border-right:5px solid #d8b88a}
.box{position:absolute;top:765px;width:335px;height:214px;background:var(--panel);border-radius:12px}
.box h2{position:absolute;top:10px;font-family:"Source Sans 3",sans-serif;font-weight:600;font-size:21px;color:var(--blue);letter-spacing:.3px}
.box ul{position:absolute;list-style:none;font-size:14.5px;color:var(--text)}
.box li{height:26px;padding-left:22px;position:relative}
.box li::before{content:"";position:absolute;left:0;top:5px;border-left:5px solid var(--blue);border-top:4px solid transparent;border-bottom:4px solid transparent}
.footer{position:absolute;left:0;top:1014px;width:1200px;height:96px;background:var(--footer);color:#fff;text-align:center;font-size:12.5px}
.footer .links{position:absolute;top:29px;width:100%}
.footer .links i{font-style:normal;margin:0 11px}
.footer .copy{position:absolute;top:51px;width:100%}
</style>
</head>
<body>
<div class="side-art" style="left:0;top:0;width:101px;height:300px" role="img" aria-label="Stacked notebooks along the left edge"></div>
<div class="side-art" style="left:1099px;top:720px;width:101px;height:275px" role="img" aria-label="Stacked notebooks along the right edge"></div>

<div class="page">
  <header class="header">
    <div class="brand"><span class="brand-dot"></span>Quill Number Desk</div>
    <div class="connect">Connect us</div>
    <div class="icons">
      <svg width="26" height="26"><circle cx="13" cy="13" r="12" fill="#8a8a8a"/></svg>
      <svg width="26" height="26"><circle cx="13" cy="13" r="12" fill="#8a8a8a"/></svg>
      <svg width="30" height="26"><rect x="1" y="2" width="28" height="22" fill="#8a8a8a"/><path d="M1 2 L15 14 L29 2" stroke="#fff" stroke-width="1.5" fill="none"/></svg>
      <svg width="24" height="28"><rect x="1" y="1" width="22" height="26" rx="3" fill="#8a8a8a"/><rect x="5" y="5" width="14" height="6" fill="#fff"/><g fill="#fff"><rect x="5" y="14" width="4" height="3"/><rect x="10" y="14" width="4" height="3"/><rect x="15" y="14" width="4" height="3"/><rect x="5" y="20" width="4" height="3"/><rect x="10" y="20" width="4" height="3"/><rect x="15" y="20" width="4" height="3"/></g></svg>
    </div>
    <div class="search">-----search here---------------</div>
    <div class="go">GO</div>
  </header>

  <nav class="nav">
    <a class="active" style="left:15px;width:84px">Home</a>
    <a style="left:116px;width:103px">Algebra</a>
    <a style="left:219px;width:120px">Geometry</a>
    <a style="left:339px;width:87px">Trig</a>
    <a style="left:426px;width:110px">Calculus</a>
    <a style="left:536px;width:103px">Statistics</a>
    <a style="left:639px;width:100px">More</a>
    <a style="left:739px;width:118px">Subjects</a>
    <a style="left:857px;width:141px">Message Board</a>
  </nav>

  <aside class="ad">
    <div class="ad-head">Vacune a<br>de los 2 años.</div>
    <div class="ad-photo" role="img" aria-label="Family photo with parents and two young children above a heart illustration"></div>
    <div class="ad-band">Para mas información llame al</div>
    <div class="ad-foot"></div>
    <div class="ad-phone">1-800-555-0142</div>
    <div class="ad-small">Su llamada es gratis, confidencial y en español.</div>
    <div class="ad-url">www.vacunafamilia.org</div>
    <div class="ad-badge"></div>
  </aside>

  <div class="chat-art" role="img" aria-label="Support agent with a speech bubble"></div>
  <div class="chat"><b>LIVE CHAT</b>Live Chat with our Staff<br>Mon - Fri 8.30am - 4.00pm</div>

  <div class="hero"><div class="hero-photo" role="img" aria-label="Group of smiling students with backpacks outdoors"></div></div>

  <h1 class="welcome">Welcome to <span>Quill Number Desk!</span></h1>
  <p class="intro" style="left:227px;top:552px">Math Lessons - Looking to understand a subject better, or maybe you don't understand what your textbook is trying to tell you? We have a collection of algebra and geometry lessons that you can view online right now.</p>
  <p class="intro" style="left:232px;top:640px">Math Lessons - Looking to understand a subject better, or maybe you don't understand what your textbook is trying to tell you? We have a collection of algebra and geometry lessons that you can view online right now.</p>
  <div class="study-photo" role="img" aria-label="Student studying with a book in front of a chalkboard of integrals"></div>

  <section class="box" style="left:236px">
    <h2 style="left:17px">What's New?</h2>
    <ul style="left:20px;top:60px">
      <li>Multiplying Polynomials</li>
      <li>Derivative of an Inverse Function</li>
      <li>Derivatives of Logs and Exps</li>
      <li>Differentiating Trig Functions</li>
    </ul>
  </section>
  <section class="box" style="left:627px">
    <h2 style="left:22px">Math Lessons</h2>
    <ul style="left:22px;top:50px">
      <li>Algebra</li><li>Geometry</li><li>Trigonometry</li><li>Calculus</li><li>Statistics</li>
    </ul>
    <ul style="left:202px;top:50px">
      <li>Sports Math</li><li>Math Games</li><li>Calculators</li>
    </ul>
  </section>
</div>

<footer class="footer">
  <div class="links">Home<i>|</i>Algebra<i>|</i>Geometry<i>|</i>Trig<i>|</i>Calculus<i>|</i>Statistics<i>|</i>More<i>|</i>Subjects<i>|</i>Message Board</div>
  <div class="copy">© Copyright 2006-2013 QuillNumberDesk.com</div>
</footer>
</body>
</html>
```